Clever & creative business card needed for a pediatric dentist.

We need a business card for a pediatric dentist that is building a brand-new pediatric dental practice. He is funny, outgoing, and sociable, and he hopes to give his business card to dentists and pediatricians so that he can give them information of where to refer infants, children, and teenagers that need high quality and attainable dental care.

The name of the dental practice is Copper Fern Pediatric Dentistry. Logo design .png / .pdf/ .jpg are provided to aid in the design.

The dentist's last name is Tolvan (which sounds like "burger", as in "hamburger” or “cheeseburger"). Since it is pediatric practice, kudos will be given to designs that implement a little joke into the design - but hopefully in a small or hidden way (such as putting something like a cheeseburger on the back of the card, or hiding it an an abstract way).

Thank you!

Please make a design that incorporates colors. It should be fun! Not too serious. It does not have to follow the color scheme of the logos.

```html
<!DOCTYPE html>
<html lang="en">
<head>
<meta charset="utf-8">
<title>Copper Fern Pediatric Dentistry – Business Card</title>
<link rel="stylesheet" href="https://fonts.googleapis.com/css2?family=Ubuntu:wght@400;500&family=Quicksand:wght@500&display=swap">
<style>
  :root {
    --backdrop: #b3b3b3;
    --white: #ffffff;
    --charcoal: #4a4a4c;
    --ink: #3c3c3e;
    --mint: #b5dcb7;
    --leaf: #8fce98;
    --forest: #449b62;
    --warm-brown: #77594a;
    --warm-grey: #5f5450;
  }
  * { box-sizing: border-box; margin: 0; padding: 0; }
  html, body {
    width: 1000px; height: 1200px; overflow: hidden;
    background: var(--backdrop);
  }
  .sheet { position: relative; width: 1000px; height: 1200px; }
  .card {
    position: absolute; left: 51px; width: 898px; height: 538px;
    overflow: hidden;
  }
  .card--front { top: 44px; background: var(--white); }
  .card--back { top: 618px; background: var(--charcoal); }
  .waves { position: absolute; inset: 0; width: 898px; height: 538px; }

  .brand {
    position: absolute; text-align: center;
    font-family: "Quicksand", sans-serif; font-weight: 500;
  }
  .brand__mark {
    width: 108px; height: 108px; border-radius: 50%;
    background: var(--leaf); margin: 0 auto 26px;
  }
  .brand__name { font-size: 52px; line-height: 1; letter-spacing: 1px; }
  .brand__tag { font-size: 17px; letter-spacing: 6.6px; margin-top: 12px; }
  .card--front .brand { left: 41px; top: 160px; width: 400px; color: var(--charcoal); }
  .card--back .brand { left: 248px; top: 162px; width: 400px; color: var(--white); }

  .contact {
    position: absolute; left: 508px; top: 148px;
    font-family: "Ubuntu", sans-serif; color: var(--ink);
  }
  .contact__name { font-size: 29px; font-weight: 500; line-height: 1.25; }
  .contact__role { font-size: 29px; font-weight: 400; line-height: 1.25; margin-bottom: 14px; }
  .contact__list { list-style: none; }
  .contact__item {
    display: flex; align-items: center; gap: 10px;
    font-size: 25px; line-height: 1; height: 44px;
  }
  .contact__icon {
    width: 28px; height: 28px; border-radius: 3px; background: var(--forest);
    display: flex; align-items: center; justify-content: center; flex: none;
  }
  .contact__icon svg { width: 18px; height: 18px; }

  .illustration {
    position: absolute; top: 118px; height: 300px;
    opacity: .85;
  }
  .illustration--left {
    left: 0; width: 216px;
    background: linear-gradient(90deg, var(--warm-brown), var(--warm-grey));
  }
  .illustration--right {
    left: 700px; width: 198px;
    background: linear-gradient(90deg, var(--warm-grey), var(--warm-brown));
  }
</style>
</head>
<body>
<main class="sheet">

  <section class="card card--front">
    <svg class="waves" viewBox="0 0 898 538" aria-hidden="true">
      <path d="M0 0 H898 V64 C800 40 720 18 640 22 C480 30 300 90 118 85 C70 84 30 76 0 66 Z" fill="var(--mint)"/>
      <path d="M0 474 C90 500 180 516 270 516 C450 516 620 453 778 453 C830 453 870 462 898 474 V538 H0 Z" fill="var(--forest)"/>
    </svg>

    <div class="brand">
      <div class="brand__mark"></div>
      <p class="brand__name">copper fern</p>
      <p class="brand__tag">PEDIATRIC DENTISTRY</p>
    </div>

    <div class="contact">
      <p class="contact__name">Your Name</p>
      <p class="contact__role">Manager</p>
      <ul class="contact__list">
        <li class="contact__item">
          <span class="contact__icon"><svg viewBox="0 0 24 24"><path d="M6.6 2.5l3 3.6-1.8 2.3c1.2 2.6 3.2 4.6 5.8 5.8l2.3-1.8 3.6 3-2 3.8C10.5 18.7 5.3 13.5 2.8 4.5Z" fill="none" stroke="#fff" stroke-width="1.8" stroke-linejoin="round"/></svg></span>
          123 444 555
        </li>
        <li class="contact__item">
          <span class="contact__icon"><svg viewBox="0 0 24 24"><path d="M12 22c-4-5-6-8.5-6-12a6 6 0 0 1 12 0c0 3.5-2 7-6 12Z" fill="none" stroke="#fff" stroke-width="1.8"/><circle cx="12" cy="10" r="2.2" fill="#fff"/></svg></span>
          789 Your Street Here
        </li>
        <li class="contact__item">
          <span class="contact__icon"><svg viewBox="0 0 24 24"><rect x="3" y="6" width="18" height="12" fill="none" stroke="#fff" stroke-width="1.8"/><path d="M3 6l9 7 9-7M3 18l7-6M21 18l-7-6" fill="none" stroke="#fff" stroke-width="1.6"/></svg></span>
          info@yourname.com
        </li>
        <li class="contact__item">
          <span class="contact__icon"><svg viewBox="0 0 24 24"><circle cx="12" cy="12" r="9" fill="none" stroke="#fff" stroke-width="1.8"/><ellipse cx="12" cy="12" rx="4" ry="9" fill="none" stroke="#fff" stroke-width="1.5"/><path d="M3 12h18M5 7.5h14M5 16.5h14" stroke="#fff" stroke-width="1.5"/></svg></span>
          www.yourname.com
        </li>
      </ul>
    </div>
  </section>

  <section class="card card--back">
    <svg class="waves" viewBox="0 0 898 538" aria-hidden="true">
      <path d="M0 0 H898 V63 C860 76 830 85 795 85 C600 85 420 21 254 21 C160 21 70 40 0 63 Z" fill="var(--mint)"/>
      <path d="M0 474 C40 462 90 453 135 453 C330 453 520 516 710 516 C790 516 850 495 898 474 V538 H0 Z" fill="var(--forest)"/>
    </svg>

    <div class="illustration illustration--left" role="img" aria-label="Cheeseburger illustration, cut by the left edge"></div>
    <div class="illustration illustration--right" role="img" aria-label="Cheeseburger illustration, cut by the right edge"></div>

    <div class="brand">
      <div class="brand__mark"></div>
      <p class="brand__name">copper fern</p>
      <p class="brand__tag">PEDIATRIC DENTISTRY</p>
    </div>
  </section>

</main>
</body>
</html>
```